Computer Company needs a Business card design

We need a business card design for our business. We assist people to transition to the QTG (Quillary Telelink Grid). The Australian Government-owned qtg™ network is a brand new telecommunications network currently being rolled out across Australia, giving access to a reliable broadband connection. Our niche market will predominantly be domestic customers in the 50+ age bracket. The assistance that we provide is everything from arranging the equipment, arranging the plan and contract term, appointment times, final testing of the network and any tweaks that need to be made. We basically PM the transition from start to finish. The business card design should be minimalist, should communicate loyalty and stability, should be easy to read and clearly explain what we do. We have asked for front and back. However, the back of the card does not have to include much information at all. It could be just a small design, or a repeat of our phone number. Up to you. The attached file only says what is required on the card. It does not specify where to arrange the text, what fonts to use, etc etc. As much as we would like to give you more info, due to our very limited design ability, we are not really able to send you any rough, or otherwise, designs of what we are after. Hopefully the above description is enough for you.

```html
<!DOCTYPE html>
<html lang="en">
<head>
<meta charset="utf-8">
<title>qtg Made Easy – Business Card</title>
<link rel="stylesheet" href="https://fonts.googleapis.com/css2?family=Exo+2:wght@400;500;600&display=swap">
<style>
  :root {
    --backdrop: #efeff1;
    --card-black: #0d0d0d;
    --card-white: #ffffff;
    --ink: #111111;
    --accent-red: #c8321f;
    --paper-edge: #dcdcde;
  }
  * { box-sizing: border-box; margin: 0; padding: 0; }
  html, body {
    width: 1200px;
    height: 1000px;
    overflow: hidden;
    background: var(--backdrop);
    font-family: "Exo 2", sans-serif;
  }
  .card-set {
    position: absolute;
    top: 345px;
    left: 80px;
    display: flex;
    gap: 40px;
  }
  .card {
    width: 500px;
    height: 300px;
    position: relative;
  }
  /* Front */
  .card-front {
    background: var(--card-black);
    display: flex;
    align-items: center;
    justify-content: center;
    gap: 22px;
  }
  .front-brand {
    color: var(--card-white);
    font-size: 92px;
    font-weight: 400;
    letter-spacing: 1px;
    line-height: 1;
  }
  .front-dot {
    width: 26px;
    height: 26px;
    border-radius: 50%;
    background: var(--card-white);
  }
  /* Back */
  .card-back {
    background: var(--card-white);
    border: 1px solid var(--paper-edge);
  }
  .tagline-row {
    position: absolute;
    top: 44px;
    left: 34px;
    right: 34px;
    display: flex;
    align-items: center;
    gap: 14px;
  }
  .tagline-rule {
    flex: 1;
    height: 2px;
    background: var(--ink);
  }
  .tagline {
    font-size: 13px;
    font-weight: 500;
    color: var(--ink);
    white-space: nowrap;
  }
  .tagline .highlight { color: var(--accent-red); }
  .back-brand {
    position: absolute;
    top: 126px;
    left: 0;
    right: 0;
    display: flex;
    align-items: center;
    justify-content: center;
    gap: 8px;
  }
  .back-brand-name {
    font-size: 26px;
    font-weight: 500;
    color: var(--ink);
  }
  .back-brand-dot {
    width: 9px;
    height: 9px;
    border-radius: 50%;
    background: var(--ink);
  }
  .contact-row {
    position: absolute;
    bottom: 38px;
    left: 34px;
    right: 34px;
    display: flex;
    align-items: center;
    gap: 12px;
    font-size: 14px;
    font-weight: 500;
    color: var(--ink);
    white-space: nowrap;
  }
  .contact-name { color: var(--accent-red); }
  .contact-divider { color: var(--ink); }
  .contact-phone { font-size: 16px; }
</style>
</head>
<body>
  <main class="card-set">
    <section class="card card-front" aria-label="Card front">
      <span class="front-brand">qtgME</span>
      <span class="front-dot" aria-hidden="true"></span>
    </section>

    <section class="card card-back" aria-label="Card back">
      <div class="tagline-row">
        <span class="tagline-rule"></span>
        <p class="tagline">Quillary Telelink Grid <span class="highlight">Made Easy</span></p>
        <span class="tagline-rule"></span>
      </div>

      <div class="back-brand">
        <span class="back-brand-name">qtgME</span>
        <span class="back-brand-dot" aria-hidden="true"></span>
      </div>

      <div class="contact-row">
        <span class="contact-name">Owen Marlowe</span>
        <span class="contact-divider">|</span>
        <span class="contact-web">www.qtgmadeeasy.example.au</span>
        <span class="contact-divider">|</span>
        <span class="contact-phone">040 555 0192</span>
      </div>
    </section>
  </main>
</body>
</html>
```